Business Card Design

We need a business card design for a consulting firm which provides safety and risk management consulting services for public venues, hotels and tourist attractions. The business card design should include the attached logo unedited with a design based on incorporating the existing logo with a design of geometric patterns or lines on a predominantly white background.

Industry/Entity Type

Business

Contact Information for Business Card

Dane Morvello
Director & Principal Consultant

Ph: +61 (0) 468502 174
PO Box 456 Kellmore Vale, NSW Australia 2563
info@corvanwellandcare.com

(back of card to include website www.corvanwellandcare.com

```html
<!DOCTYPE html>
<html lang="en">
<head>
<meta charset="utf-8">
<title>Corvan Welland Care – Business Card</title>
<link href="https://fonts.googleapis.com/css2?family=Open+Sans:wght@400;600;700&display=swap" rel="stylesheet">
<style>
  :root {
    --backdrop: #e9e7e3;
    --card-white: #ffffff;
    --brand-blue: #2596d6;
    --brand-green: #6cbf3a;
    --brand-grey: #8a8482;
    --ink: #1d1d1d;
    --on-blue: #ffffff;
  }
  * { box-sizing: border-box; margin: 0; padding: 0; }
  html, body {
    width: 1200px; height: 900px; overflow: hidden;
    background: var(--backdrop);
    font-family: "Open Sans", Arial, sans-serif;
  }
  .canvas { position: relative; width: 1200px; height: 900px; }
  .card {
    position: absolute; width: 520px; height: 297px;
    background: var(--card-white);
    box-shadow: 0 6px 18px rgba(0,0,0,.18);
    overflow: hidden;
  }
  .card--back { left: 70px; top: 150px; }
  .card--front { left: 610px; top: 453px; }

  .brand {
    display: flex; align-items: center; gap: 12px;
    font-weight: 700; letter-spacing: .5px; white-space: nowrap;
  }
  .brand__dot { width: 26px; height: 26px; border-radius: 50%; flex: none; }
  .brand__name { font-size: 30px; }

  .card--back .brand { position: absolute; left: 0; right: 0; top: 98px; justify-content: center; }
  .card--back .brand__dot { background: var(--brand-grey); }
  .card--back .brand__name { color: var(--brand-grey); }
  .website {
    position: absolute; left: 0; right: 0; top: 196px;
    text-align: center; font-size: 15px; font-weight: 600; color: var(--ink);
  }

  .card--front .brand { position: absolute; left: 0; right: 0; top: 52px; justify-content: center; }
  .card--front .brand__dot { background: var(--brand-green); }
  .card--front .brand__name { color: var(--brand-blue); }

  .contact-band {
    position: absolute; left: 0; right: 0; bottom: 0; height: 163px;
    background: var(--brand-blue); color: var(--on-blue);
  }
  .person { position: absolute; left: 26px; top: 22px; }
  .person__name { font-size: 21px; font-weight: 700; }
  .person__role { font-size: 14px; margin-top: 2px; }
  .address { position: absolute; left: 26px; top: 98px; font-size: 14px; line-height: 1.4; }

  .lines {
    position: absolute; right: 22px; top: -26px;
    list-style: none; font-size: 13px; text-align: right;
  }
  .lines li { display: flex; align-items: center; justify-content: flex-end; gap: 8px; height: 22px; }
  .lines .on-white { color: var(--ink); }
  .lines .on-band { color: var(--on-blue); }
  .icon { width: 16px; height: 16px; flex: none; }
</style>
</head>
<body>
<main class="canvas">

  <section class="card card--back" aria-label="Card back">
    <div class="brand">
      <span class="brand__dot"></span>
      <span class="brand__name">Corvan Welland Care</span>
    </div>
    <p class="website">www.corvanwellandcare.com</p>
  </section>

  <section class="card card--front" aria-label="Card front">
    <div class="brand">
      <span class="brand__dot"></span>
      <span class="brand__name">Corvan Welland Care</span>
    </div>

    <div class="contact-band">
      <ul class="lines">
        <li class="on-white">+61 (0) 468502 174
          <svg class="icon" viewBox="0 0 16 16" aria-hidden="true">
            <rect width="16" height="16" rx="3" fill="#6d6d6d"/>
            <path d="M4.5 3.5l2 .3.6 2.2-1.2.9a6 6 0 0 0 3.2 3.2l.9-1.2 2.2.6.3 2c-.4.6-1.3 1-2 .9A8.3 8.3 0 0 1 3.6 5.5c-.1-.7.3-1.6.9-2z" fill="#fff"/>
          </svg>
        </li>
        <li class="on-band">info@corvanwellandcare.com
          <svg class="icon" viewBox="0 0 16 16" aria-hidden="true">
            <rect width="16" height="16" rx="3" fill="#fff"/>
            <rect x="3" y="4.5" width="10" height="7" fill="none" stroke="#2596d6" stroke-width="1.2"/>
            <path d="M3 4.5l5 4 5-4" fill="none" stroke="#2596d6" stroke-width="1.2"/>
          </svg>
        </li>
      </ul>

      <div class="person">
        <p class="person__name">Dane Morvello</p>
        <p class="person__role">Director &amp; Principal Consultant</p>
      </div>
      <p class="address">PO Box 456 Kellmore Vale,<br>NSW Australia 2563</p>
    </div>
  </section>

</main>
</body>
</html>
```